Pictures required on web page

I would like change three existing pictures on my new website.

The site can be found here:
http://mossbottleroom.kestrelweb.com.au/

The three pictures to be changed are on the home page:
Purchase- Mixed Packs
Wine Club - Let Us Choose
Education- Wine Courses

I would like somthing stylish, classic and understated that fits in with the theme and feel of the site. I know stylish is a subjective thing. At the moment, the current picture makes the text difficult to read on a destop. Plus I don't think they are a perfect fit for our website anyway. I've attached a photo of our wine course room and also me in the store. Please, don't feel as though you have to use these pictures, but they're there if you want them. However I'm open to completely different photos/graphics to be used.

```html
<!DOCTYPE html>
<html lang="en">
<head>
<meta charset="utf-8">
<title>Moss Bottle Room – Home Tiles</title>
<link href="https://fonts.googleapis.com/css2?family=Roboto+Slab:wght@700&family=Roboto:wght@300;400&display=swap" rel="stylesheet">
<style>
  :root {
    --page-bg: #ffffff;
    --club-brown: #35190f;
    --club-border: #5c4232;
    --club-muted: #cdbcae;
    --shipping-red: #b24a48;
    --newsletter-navy: #1f2d4d;
    --newsletter-sub: #b9c6dc;
    --course-gold: #f5b400;
    --button-gold: #f7b500;
    --button-navy: #0d2a5c;
    --frame-line: rgba(255, 255, 255, 0.32);
    --white: #ffffff;
  }
  * { box-sizing: border-box; margin: 0; padding: 0; }
  html, body {
    width: 1200px; height: 469px; overflow: hidden;
    background: var(--page-bg);
    font-family: "Roboto", Arial, sans-serif;
  }
  .tiles { position: relative; width: 1200px; height: 469px; }
  .tile { position: absolute; overflow: hidden; }

  /* Photo tiles */
  .tile--courses { left: 17px; top: 17px; width: 375px; height: 250px; }
  .tile--packs { left: 814px; top: 17px; width: 375px; height: 250px; }
  .photo { position: absolute; inset: 0; }
  .photo--shop-shelves {
    background:
      radial-gradient(ellipse at 25% 60%, #8a7a6c 0%, rgba(138,122,108,0) 45%),
      linear-gradient(90deg, #3a1a10 0%, #6b2a1a 40%, #4a1c12 70%, #2a120c 100%);
  }
  .photo--storefront {
    background:
      linear-gradient(180deg, #2e3658 0%, #9ea3bd 30%, #6d7291 55%, #1f2440 100%);
  }
  .photo-caption {
    position: absolute; left: 0; right: 0; text-align: center;
  }
  .tile--courses .photo-caption { top: 153px; }
  .tile--packs .photo-caption { top: 152px; }
  .caption-title {
    font-family: "Roboto Slab", Georgia, serif; font-weight: 700;
    font-size: 33px; line-height: 1; letter-spacing: -0.3px;
    text-shadow: 0 2px 4px rgba(0,0,0,0.55);
  }
  .caption-title--gold { color: var(--course-gold); }
  .caption-title--white { color: var(--white); }
  .caption-button {
    display: inline-block; margin-top: 10px;
    height: 41px; line-height: 41px; padding: 0 16px;
    font-size: 20px; color: var(--white); text-transform: uppercase;
  }
  .caption-button--gold { background: var(--button-gold); }
  .caption-button--navy { background: var(--button-navy); }

  /* Wine club */
  .tile--club { left: 415px; top: 17px; width: 375px; height: 437px; background: var(--club-brown); }
  .club-header { height: 97px; text-align: center; padding-top: 14px; color: var(--white); }
  .club-title {
    font-family: "Roboto Slab", Georgia, serif; font-weight: 700;
    font-size: 39px; line-height: 1;
  }
  .club-tagline { font-size: 20px; font-weight: 400; margin-top: 9px; letter-spacing: 0.5px; }
  .photo--tasting-room {
    position: absolute; left: 0; top: 102px; width: 375px; height: 258px;
    background:
      radial-gradient(ellipse at 50% 30%, #a07a4c 0%, rgba(160,122,76,0) 55%),
      linear-gradient(180deg, #3d2214 0%, #6a4428 45%, #4a2a18 70%, #2c160c 100%);
  }
  .club-footer {
    position: absolute; left: 0; right: 0; top: 367px; bottom: 0;
    display: flex; align-items: center; justify-content: center;
  }
  .club-button {
    width: 155px; height: 43px; line-height: 41px; text-align: center;
    border: 1px solid var(--club-border); color: var(--club-muted);
    font-size: 16px; text-transform: uppercase;
  }

  /* Framed info tiles */
  .tile--shipping { left: 17px; top: 285px; width: 375px; height: 169px; background: var(--shipping-red); }
  .tile--newsletter { left: 814px; top: 283px; width: 375px; height: 169px; background: var(--newsletter-navy); }
  .framed {
    position: absolute; inset: 23px 23px;
    border: 1px solid var(--frame-line);
    display: flex; flex-direction: column; align-items: center; justify-content: center;
    color: var(--white); text-align: center;
  }
  .framed-title { font-size: 23px; font-weight: 400; letter-spacing: 2px; text-transform: uppercase; }
  .framed-sub { font-size: 15px; font-weight: 300; letter-spacing: 1.4px; margin-top: 9px; }
  .tile--newsletter .framed-sub { color: var(--newsletter-sub); }
</style>
</head>
<body>
<main class="tiles">
  <a class="tile tile--courses">
    <div class="photo photo--shop-shelves" role="img" aria-label="Shop owner standing beside shelves of wine bottles"></div>
    <div class="photo-caption">
      <div class="caption-title caption-title--gold">Wine Courses</div>
      <span class="caption-button caption-button--gold">Education</span>
    </div>
  </a>

  <section class="tile tile--club">
    <header class="club-header">
      <h2 class="club-title">Wine Club</h2>
      <p class="club-tagline">LET US CHOOSE</p>
    </header>
    <div class="photo--tasting-room" role="img" aria-label="Tasting room with a long table and chairs in front of a wall of wine racks"></div>
    <div class="club-footer"><span class="club-button">Read More</span></div>
  </section>

  <a class="tile tile--packs">
    <div class="photo photo--storefront" role="img" aria-label="Blue-toned street view of the wine shop front"></div>
    <div class="photo-caption">
      <div class="caption-title caption-title--white">Mixed Packs</div>
      <span class="caption-button caption-button--navy">Purchase</span>
    </div>
  </a>

  <section class="tile tile--shipping">
    <div class="framed">
      <h3 class="framed-title">Free Shipping</h3>
      <p class="framed-sub">on orders over $200</p>
    </div>
  </section>

  <section class="tile tile--newsletter">
    <div class="framed">
      <h3 class="framed-title">Newsletter</h3>
      <p class="framed-sub">join the newsletter for specials</p>
    </div>
  </section>
</main>
</body>
</html>
```